Harbel Shipping

A flyer that sells both air and sea freight services. We had an attempt at this and wanted a fresh concept from your designers. Colors should be vibrant and the text readable on a digital billboard as well. Our attempt is attached along with our logo file.

Designers***The contents on our attempt flyer should be applied to your flyer design.

Thanks!

Industry/Entity Type

Shipping

```html
<!DOCTYPE html>
<html lang="en">
<head>
<meta charset="utf-8">
<title>Harbel Shipping – Air &amp; Sea Freight Flyer</title>
<link rel="stylesheet" href="https://fonts.googleapis.com/css2?family=Exo+2:wght@600;700&family=Oswald:wght@400;500;600&family=Lato:wght@400;700&family=Montserrat:wght@800&display=swap">
<style>
  :root {
    --white: #ffffff;
    --brand-red: #9e1b20;
    --accent-red: #d3262c;
    --navy: #0d2748;
    --navy-deep: #0a1f3c;
    --mid-blue: #1f5f9f;
    --sea-blue: #2c7bb3;
    --hex-fill: #ececec;
    --ink: #2b2b2b;
    --text-dark: #1e2a3a;
    --silver: #d9dde2;
  }
  * { box-sizing: border-box; margin: 0; padding: 0; }
  html, body { width: 902px; height: 1200px; overflow: hidden; background: #f2f2f2; }
  .flyer { position: relative; width: 902px; height: 1200px; background: var(--white); overflow: hidden; font-family: "Lato", Arial, sans-serif; }

  .photo-containers {
    position: absolute; left: 0; top: 0; width: 902px; height: 340px;
    clip-path: polygon(330px 0, 902px 0, 902px 143px, 330px 266px);
    background: linear-gradient(100deg, rgba(255,255,255,1) 0%, #c9d6e3 30%, #b88a72 65%, #f3c98e 100%);
  }
  .band-mid {
    position: absolute; inset: 0;
    clip-path: polygon(0 337px, 902px 143px, 902px 536px, 0 707px);
    background: linear-gradient(180deg, var(--sea-blue) 0%, var(--mid-blue) 60%, #1a4f8c 100%);
  }
  .photo-ship {
    position: absolute; inset: 0;
    clip-path: polygon(420px 250px, 902px 148px, 902px 536px, 600px 594px);
    background: linear-gradient(160deg, #3a86b8 0%, #b8455a 45%, #d97a4a 70%, #2f6e9c 100%);
    opacity: .85;
  }
  .band-navy {
    position: absolute; inset: 0;
    clip-path: polygon(0 707px, 902px 536px, 902px 1006px, 0 1006px);
    background: linear-gradient(180deg, var(--navy-deep) 0%, var(--navy) 100%);
  }
  .photo-port {
    position: absolute; left: 0; top: 800px; width: 340px; height: 206px;
    background: linear-gradient(90deg, rgba(46,110,170,.85) 0%, rgba(36,90,150,.55) 60%, rgba(13,39,72,0) 100%);
  }

  .brand { position: absolute; left: 70px; top: 60px; display: flex; flex-direction: column; align-items: center; gap: 14px; }
  .brand-dot { width: 120px; height: 120px; border-radius: 50%; border: 6px solid var(--brand-red); }
  .brand-name { font-family: "Exo 2", sans-serif; font-weight: 700; font-size: 40px; line-height: 1.05; color: var(--brand-red); text-align: center; text-transform: uppercase; }

  .hero-title { position: absolute; left: 50px; top: 372px; font-family: "Exo 2", sans-serif; font-weight: 600; font-size: 49px; line-height: 64px; color: var(--white); text-transform: uppercase; }
  .hero-copy { position: absolute; left: 52px; top: 504px; width: 480px; font-family: "Exo 2", sans-serif; font-weight: 600; font-size: 15.5px; line-height: 21px; color: var(--white); }

  .discount { position: absolute; left: 120px; top: 634px; width: 298px; height: 258px; }
  .discount svg { position: absolute; inset: 0; }
  .discount-text { position: absolute; inset: 0; display: flex; flex-direction: column; align-items: center; padding-top: 34px; text-align: center; }
  .discount-amount { font-family: "Oswald", sans-serif; font-weight: 600; font-size: 62px; line-height: 70px; color: var(--accent-red); }
  .discount-label { font-family: "Oswald", sans-serif; font-weight: 500; font-size: 33px; line-height: 36px; color: var(--ink); letter-spacing: .5px; }
  .discount-note { margin-top: 6px; font-family: Arial, sans-serif; font-size: 15px; line-height: 17px; color: var(--accent-red); text-transform: uppercase; }

  .offer-kicker { position: absolute; left: 481px; top: 602px; font-family: "Oswald", sans-serif; font-weight: 500; font-size: 34px; line-height: 40px; color: var(--white); text-transform: uppercase; }
  .offer-title { position: absolute; left: 480px; top: 648px; font-family: "Oswald", sans-serif; font-weight: 600; font-size: 73px; line-height: 76px; color: var(--white); text-transform: uppercase; letter-spacing: .5px; }

  .offer-pill { position: absolute; left: 477px; top: 750px; width: 300px; height: 76px; border-radius: 8px; background: linear-gradient(180deg, #e33a3d 0%, #b71d23 100%); color: var(--white); padding: 10px 0 0 22px; text-transform: uppercase; }
  .offer-pill .line-1 { font-family: "Lato", sans-serif; font-size: 23px; line-height: 28px; }
  .offer-pill .line-2 { font-family: "Lato", sans-serif; font-size: 18px; line-height: 24px; }
  .offer-badge { position: absolute; left: 737px; top: 726px; width: 116px; height: 116px; border-radius: 50%; background: var(--silver); border: 3px solid #8c939b; display: flex; align-items: center; justify-content: center; }
  .offer-badge span { width: 96px; height: 96px; border-radius: 50%; background: radial-gradient(circle at 40% 35%, #f04a46 0%, #c2161d 70%); display: flex; flex-direction: column; align-items: center; justify-content: center; font-family: "Oswald", sans-serif; font-weight: 500; font-size: 23px; line-height: 25px; color: var(--white); text-transform: uppercase; }

  .offer-copy { position: absolute; left: 366px; top: 856px; width: 476px; font-family: "Lato", sans-serif; font-weight: 700; font-size: 15.5px; line-height: 21px; color: var(--white); text-align: justify; hyphens: auto; }

  .contact-row { position: absolute; left: 0; top: 1006px; width: 902px; height: 88px; background: var(--white); }
  .contact-item { position: absolute; top: 28px; display: flex; align-items: flex-start; gap: 14px; font-family: "Lato", sans-serif; font-size: 13px; line-height: 16px; color: var(--text-dark); }
  .contact-item svg { flex: none; width: 30px; height: 30px; margin-top: -4px; }
  .contact-item.home { left: 62px; width: 220px; }
  .contact-item.mail { left: 334px; }
  .contact-item.web { left: 628px; }

  .call-bar { position: absolute; left: 0; top: 1094px; width: 902px; height: 106px; background: var(--brand-red); display: flex; align-items: center; justify-content: center; gap: 16px; color: var(--white); font-family: "Montserrat", sans-serif; font-weight: 800; }
  .call-label { font-size: 37px; }
  .call-icon { width: 56px; height: 56px; }
  .call-number { font-size: 58px; letter-spacing: 1px; }
</style>
</head>
<body>
<main class="flyer">
  <div class="photo-containers" role="img" aria-label="Photo of stacked shipping containers at a port with a cargo plane flying in a sunlit sky"></div>
  <div class="band-mid"></div>
  <div class="photo-ship" role="img" aria-label="Aerial photo of a container ship loaded with colourful containers sailing on blue sea"></div>
  <div class="band-navy"></div>
  <div class="photo-port" role="img" aria-label="Photo of port cranes loading a container vessel at dusk"></div>

  <div class="brand">
    <div class="brand-dot"></div>
    <div class="brand-name">Harbel<br>Shipping</div>
  </div>

  <h1 class="hero-title">Lorem Ipsum<br>is simply dummy</h1>
  <p class="hero-copy">Lorem Ipsum has been the industry's standard dummy text ever since the 1500s, when an unknown printer took a galley of type and scrambled it to make a type specimen book.</p>

  <div class="discount">
    <svg viewBox="0 0 298 258" aria-hidden="true">
      <polygon points="149,0 298,66 298,192 149,258 0,192 0,66" fill="var(--hex-fill)"/>
      <polygon points="149,14 284,74 284,184 149,244 14,184 14,74" fill="none" stroke="#555" stroke-width="3" stroke-dasharray="9 6"/>
    </svg>
    <div class="discount-text">
      <div class="discount-amount">$000</div>
      <div class="discount-label">DISCOUNT</div>
      <div class="discount-note">Lorem ipsum is<br>simply dummy<br>text</div>
    </div>
  </div>

  <h2 class="offer-kicker">Lorem ipsum is simply</h2>
  <div class="offer-title">Dummy text</div>

  <div class="offer-pill">
    <div class="line-1">Lorem ipsum is</div>
    <div class="line-2">Simply dummy text</div>
  </div>
  <div class="offer-badge"><span>Up to<br>$100 off</span></div>

  <p class="offer-copy">Lorem Ipsum is simply dummy text of the printing and typesetting industry. Lorem Ipsum has been the industry's standard dummy text ever since the 1500s, when an unknown printer took a galley of type and scrambled it to make a type specimen book</p>

  <section class="contact-row">
    <div class="contact-item home">
      <svg viewBox="0 0 30 30" aria-hidden="true"><circle cx="15" cy="15" r="14" fill="var(--accent-red)"/><path d="M8 15 L15 9 L22 15 M10 14 V21 H20 V14" fill="none" stroke="#fff" stroke-width="2"/></svg>
      <span>Lorem Ipsum is simply<br>dummy text</span>
    </div>
    <div class="contact-item mail">
      <svg viewBox="0 0 30 30" aria-hidden="true"><circle cx="15" cy="15" r="14" fill="var(--accent-red)"/><rect x="8" y="10" width="14" height="10" fill="#fff"/><path d="M8 10 L15 16 L22 10" fill="none" stroke="var(--accent-red)" stroke-width="1.5"/></svg>
      <span>Lorem Ipsum is simply dummy text</span>
    </div>
    <div class="contact-item web">
      <svg viewBox="0 0 30 30" aria-hidden="true"><circle cx="15" cy="15" r="14" fill="var(--accent-red)"/><g fill="none" stroke="#fff" stroke-width="1.5"><circle cx="15" cy="15" r="7"/><ellipse cx="15" cy="15" rx="3" ry="7"/><path d="M8 15 H22"/></g></svg>
      <span>Lorem Ipsum is simply dummy text</span>
    </div>
  </section>

  <footer class="call-bar">
    <span class="call-label">CALL US !</span>
    <svg class="call-icon" viewBox="0 0 56 56" aria-hidden="true">
      <circle cx="28" cy="28" r="25" fill="none" stroke="#1a1a1a" stroke-width="4"/>
      <path d="M20 15 c2-1 4 0 5 2 l2 4 c1 2 0 3-1 4 l-2 1 c1 4 4 7 8 8 l1-2 c1-1 2-2 4-1 l4 2 c2 1 3 3 2 5 l-1 2 c-2 2-5 3-8 2 c-8-3-14-9-17-17 c-1-3 0-6 2-8 z" fill="#1a1a1a"/>
    </svg>
    <span class="call-number">0123456789</span>
  </footer>
</main>
</body>
</html>
```